Lumo4Kart - a fintech company - business card

We need a business card design for our Payments Technology company in Sydney, Australia. We provide business with payment solutions expanding across EFTPOS machines, online payment gateways and mobile payment solutions. We would like to see designs that are clean, classy and professional.
Target Market(s)
Business professionals, executives, c-suite
Industry/Entity Type
Fintech
Contact Information for Business Card
Will be on 400gsm. Logo will most likely be spot gloss unless designer recommends otherwise.
Font styles to use
Sans Serif
Requirements
Must have
- We need our website (lumo4kart.com.au), email (contact@lumo4kart.com.au), mobile (0432 587 904) and direct phone number (02 6815 3927) to feature on the card along with our logo (attached) and the words "EFTPOS | ONLINE | MOBILE"
- Font = Roboto

```html
<!DOCTYPE html>
<html lang="en">
<head>
<meta charset="utf-8">
<title>Lumo4Kart Business Card</title>
<link href="https://fonts.googleapis.com/css2?family=Roboto:wght@400;500;700&display=swap" rel="stylesheet">
<style>
  :root {
    --backdrop: #a2a2a2;
    --card-white: #ffffff;
    --brand-blue: #1d5f95;
    --brand-blue-light: #2873ab;
    --brand-blue-dark: #17507f;
    --text-grey: #4d4d4d;
    --rule-grey: #8a8a8a;
  }
  * { margin: 0; padding: 0; box-sizing: border-box; }
  html, body {
    width: 1200px;
    height: 1200px;
    overflow: hidden;
  }
  body {
    position: relative;
    background: var(--backdrop);
    font-family: "Roboto", Arial, sans-serif;
  }
  .card {
    position: absolute;
    left: 198px;
    width: 804px;
    height: 458px;
    border-radius: 24px;
    overflow: hidden;
  }
  .card--front { top: 86px; background: var(--card-white); }
  .card--back {
    top: 655px;
    background: radial-gradient(ellipse at 50% 42%, var(--brand-blue-light) 0%, var(--brand-blue) 45%, var(--brand-blue-dark) 100%);
  }

  /* Front: brand block */
  .brand {
    position: absolute;
    left: 40px;
    top: 128px;
    width: 280px;
    text-align: center;
  }
  .brand__mark {
    display: block;
    width: 84px;
    height: 84px;
    margin: 0 auto 22px;
    border-radius: 50%;
    background: var(--brand-blue);
  }
  .brand__name {
    font-weight: 500;
    font-size: 42px;
    line-height: 1;
    color: var(--brand-blue);
  }
  .services {
    margin-top: 14px;
    font-size: 15px;
    letter-spacing: 1px;
    color: var(--text-grey);
    white-space: nowrap;
  }

  .divider {
    position: absolute;
    left: 398px;
    top: 132px;
    width: 1.5px;
    height: 192px;
    background: var(--rule-grey);
  }

  /* Front: person + contacts */
  .person {
    position: absolute;
    left: 430px;
    top: 128px;
  }
  .person__name {
    font-size: 26px;
    font-weight: 400;
    color: var(--brand-blue);
    letter-spacing: 0.3px;
    line-height: 1.1;
  }
  .person__name strong { font-weight: 700; }
  .person__role {
    margin-top: 6px;
    font-size: 18px;
    color: var(--text-grey);
  }
  .contacts {
    list-style: none;
    margin-top: 34px;
  }
  .contacts__item {
    display: flex;
    align-items: center;
    height: 28.5px;
    font-size: 18px;
    color: var(--text-grey);
  }
  .contacts__icon {
    width: 16px;
    height: 16px;
    margin-right: 14px;
    flex: none;
    fill: none;
    stroke: var(--brand-blue);
    stroke-width: 1.8;
    stroke-linecap: round;
    stroke-linejoin: round;
  }

  /* Back */
  .back-brand {
    position: absolute;
    left: 0;
    right: 0;
    top: 130px;
    text-align: center;
    color: var(--card-white);
  }
  .back-brand__mark {
    display: block;
    width: 104px;
    height: 104px;
    margin: 0 auto 28px;
    border-radius: 50%;
    background: var(--card-white);
  }
  .back-brand__name {
    font-weight: 500;
    font-size: 54px;
    line-height: 1;
  }
  .back-brand .services {
    margin-top: 16px;
    font-size: 19px;
    letter-spacing: 1.2px;
    color: var(--card-white);
  }
</style>
</head>
<body>

<section class="card card--front">
  <div class="brand">
    <span class="brand__mark"></span>
    <div class="brand__name">Lumo4Kart</div>
    <div class="services">EFTPOS | ONLINE | MOBILE</div>
  </div>

  <div class="divider"></div>

  <div class="person">
    <h1 class="person__name"><strong>DANA</strong> WHITCOMBE</h1>
    <p class="person__role">Senior Consultant</p>
    <ul class="contacts">
      <li class="contacts__item">
        <svg class="contacts__icon" viewBox="0 0 16 16"><rect x="4" y="1" width="8" height="14" rx="1.5"/><line x1="7" y1="12.5" x2="9" y2="12.5"/></svg>
        (0432 587 904)
      </li>
      <li class="contacts__item">
        <svg class="contacts__icon" viewBox="0 0 16 16"><path d="M13 2.5 C8 2 3 7 3.5 13"/><path d="M11 1.5 l3 1.2 -1 2.3"/><path d="M2.3 11 l1.2 3 2.3 -1"/></svg>
        (02 6815 3927)
      </li>
      <li class="contacts__item">
        <svg class="contacts__icon" viewBox="0 0 16 16"><rect x="1.5" y="3.5" width="13" height="9" rx="0.5"/><path d="M1.5 4 L8 9 L14.5 4"/></svg>
        contact@lumo4kart.com.au
      </li>
      <li class="contacts__item">
        <svg class="contacts__icon" viewBox="0 0 16 16"><circle cx="8" cy="8" r="6.5"/><ellipse cx="8" cy="8" rx="2.8" ry="6.5"/><line x1="1.5" y1="8" x2="14.5" y2="8"/></svg>
        lumo4kart.com.au
      </li>
    </ul>
  </div>
</section>

<section class="card card--back">
  <div class="back-brand">
    <span class="back-brand__mark"></span>
    <div class="back-brand__name">Lumo4Kart</div>
    <div class="services">EFTPOS | ONLINE | MOBILE</div>
  </div>
</section>

</body>
</html>
```